Meridale Leisure Company (MLC)

We need a business card design for Meridale Leisure Company. Modern and sleek looking, with all critical information. Open to single or double sided designs, if double sided info needs to be all on one side. The main Logo is Meridale Leisure company and must be on the card. The other three logos are for the brands that fall under the group, they might be good on the back.

Industry/Entity Type

Business

```html
<!DOCTYPE html>
<html lang="en">
<head>
<meta charset="utf-8">
<title>Meridale Leisure Company – Business Card</title>
<link rel="stylesheet" href="https://fonts.googleapis.com/css2?family=Source+Sans+3:wght@400;600&display=swap">
<style>
  :root {
    --backdrop: #2e2724;
    --paper: #f7f7f5;
    --brand-blue: #2458a6;
    --brand-blue-dark: #1f4f98;
    --brand-green: #8fb12a;
    --ink-grey: #5d5d5d;
    --rule-grey: #9a9a9a;
    --band-white: #fbfbfb;
  }
  * { box-sizing: border-box; margin: 0; padding: 0; }
  html, body {
    width: 1200px; height: 844px; overflow: hidden;
    background: var(--backdrop);
    font-family: "Source Sans 3", "Myriad Pro", Arial, sans-serif;
  }
  .canvas {
    position: relative; width: 1200px; height: 844px;
  }
  .card {
    position: absolute; top: 272px;
    width: 525px; height: 300px;
    overflow: hidden;
    box-shadow: 0 14px 30px rgba(0,0,0,.45);
  }

  /* ---------- front ---------- */
  .card-front { left: 50px; background: var(--paper); }
  .brand-lockup {
    position: absolute; top: 34px; right: 34px;
    display: flex; align-items: center; gap: 10px;
  }
  .brand-lockup .brand-square {
    width: 16px; height: 16px; background: var(--brand-blue);
  }
  .brand-lockup .brand-name {
    font-size: 17px; font-weight: 600; letter-spacing: .5px;
    color: var(--brand-blue); text-transform: uppercase;
  }
  .brand-rule {
    position: absolute; top: 70px; right: 34px; width: 210px;
    border-top: 1.5px solid var(--brand-blue);
  }
  .rule {
    position: absolute; left: 34px; right: 34px;
    border-top: 1px solid var(--rule-grey);
  }
  .rule-top { top: 108px; }
  .person {
    position: absolute; left: 34px; top: 122px;
  }
  .person-name {
    font-size: 22px; font-weight: 400; letter-spacing: .3px;
    text-transform: uppercase; color: var(--brand-blue); line-height: 1;
  }
  .person-name .surname { color: var(--brand-green); }
  .person-title {
    font-size: 14px; color: var(--ink-grey); margin-top: 3px;
  }
  .rule-mid { top: 182px; }
  .address {
    position: absolute; left: 34px; top: 192px;
    font-size: 14px; color: var(--ink-grey);
  }
  .rule-low { top: 220px; }
  .contacts {
    position: absolute; left: 34px; top: 230px;
    font-size: 13.5px; color: var(--ink-grey); line-height: 1.45;
  }
  .contacts .label { color: var(--brand-blue); }
  .contacts .sep { display: inline-block; width: 10px; }
  .contacts .web { color: var(--brand-blue); }
  .contacts .web .web-name { color: var(--brand-green); }

  /* ---------- back ---------- */
  .card-back { left: 625px; background: var(--band-white); }
  .back-panel {
    position: absolute; left: 0; top: 0; width: 100%; height: 232px;
    background: linear-gradient(135deg, #2a5fae 0%, var(--brand-blue-dark) 100%);
  }
  .back-brand {
    position: absolute; left: 0; right: 0; top: 92px;
    text-align: center; color: var(--brand-green);
  }
  .back-brand .brand-name {
    font-size: 24px; font-weight: 600; letter-spacing: .5px;
    text-transform: uppercase;
  }
  .back-brand .brand-rule-pair {
    display: flex; justify-content: center; gap: 0; margin-top: 8px;
  }
  .back-brand .brand-rule-pair span {
    width: 260px; border-top: 1.5px solid var(--brand-green);
  }
  .sub-brands {
    position: absolute; left: 0; right: 0; top: 232px; bottom: 0;
    display: flex; align-items: center; justify-content: space-around;
    padding: 0 18px;
  }
  .sub-brand {
    display: flex; align-items: center; gap: 7px;
    font-size: 15px; font-weight: 600;
  }
  .sub-brand .dot { width: 14px; height: 14px; border-radius: 50%; }
  .sub-brand-terrace { color: #2b2b2b; }
  .sub-brand-terrace .dot { background: var(--brand-blue-dark); }
  .sub-brand-tickets { color: var(--brand-blue); }
  .sub-brand-tickets .dot { background: var(--brand-green); }
  .sub-brand-gate { color: var(--brand-blue-dark); }
  .sub-brand-gate .dot { background: var(--brand-blue); }
</style>
</head>
<body>
<main class="canvas">

  <section class="card card-front" aria-label="Business card front">
    <div class="brand-lockup">
      <span class="brand-square"></span>
      <span class="brand-name">Meridale Leisure Company</span>
    </div>
    <div class="brand-rule"></div>

    <div class="rule rule-top"></div>
    <div class="person">
      <p class="person-name">Daniel <span class="surname">Harper</span></p>
      <p class="person-title">Managing Director</p>
    </div>
    <div class="rule rule-mid"></div>
    <p class="address">12345, Address Goes Here Country Name, 123456.</p>
    <div class="rule rule-low"></div>
    <div class="contacts">
      <p><span class="label">T:</span>(044) 123 456 789<span class="sep"></span><span class="label">F:</span>(044) 123456789<span class="sep"></span><span class="label">M:</span> (044)123456789</p>
      <p><span class="label">E:</span>info@youremail.com<span class="sep"></span><span class="web">www.<span class="web-name">yourweb</span>.com</span></p>
    </div>
  </section>

  <section class="card card-back" aria-label="Business card back">
    <div class="back-panel"></div>
    <div class="back-brand">
      <p class="brand-name">Meridale Leisure Company</p>
      <div class="brand-rule-pair"><span></span></div>
    </div>
    <div class="sub-brands">
      <div class="sub-brand sub-brand-terrace"><span class="dot"></span>Terrace Hospitality</div>
      <div class="sub-brand sub-brand-tickets"><span class="dot"></span>MeridaleTickets</div>
      <div class="sub-brand sub-brand-gate"><span class="dot"></span>gatepoint</div>
    </div>
  </section>

</main>
</body>
</html>
```